Business Card Re-Design for a Lighting Designer

I would like my business card re-designed. It is currently high gloss and they scratch too easily. I don not think the current design lends itself well to a matte finish. I have included the current design for reference along with our company logo.
Check out our website for current branding.
http://www.brambleorchidstudio.example

Updates
Some of the top contenders are muslim and it is a holiday for them. I do not want to discriminate and would expect the same courtesy for holidays we celebrate.
Target Market(s)
Interior Designers, Architects
Contact Information for Business Card
Logo - Name, Title, Address, Telephone Number and Extension, Email
Font styles to use
Requirements
Must have
- All the information listed on the current business card. If you use Red, it needs to be the red from our logo.
Nice to have
- Vertical and Horizontal Designs will be entertained.
Should not have
- Requirements for a glossy finish...should not look too corporate since we are a design firm.

```html
<!DOCTYPE html>
<html lang="en">
<head>
<meta charset="utf-8">
<title>Bramble Orchid Studio — Business Card</title>
<link rel="stylesheet" href="https://fonts.googleapis.com/css2?family=Catamaran:wght@400;500&family=Roboto+Condensed:wght@300;400&display=swap">
<style>
  :root {
    --brand-red: #9a1b1f;
    --paper: #ffffff;
    --backdrop: #eeeeee;
    --ink: #1d1d1d;
    --muted: #8f8f8f;
    --rule-soft: #d9a3a5;
  }
  * { box-sizing: border-box; margin: 0; padding: 0; }
  html, body {
    width: 1200px; height: 1200px; overflow: hidden;
    background: var(--backdrop);
  }
  .canvas { position: relative; width: 1200px; height: 1200px; }

  .card {
    position: absolute; top: 175px; width: 499px; height: 851px;
    box-shadow: 4px 5px 10px rgba(0,0,0,0.22);
  }
  .card--front { left: 82px; background: var(--brand-red); color: var(--paper); }
  .card--back { left: 631px; background: var(--paper); color: var(--ink); }

  /* Brand lockup: square, name, optional tagline, all in normal flow */
  .brand { position: absolute; left: 130px; width: 260px; }
  .brand__mark { display: block; width: 124px; height: 124px; }
  .brand__name {
    margin-top: 16px;
    font-family: "Roboto Condensed", sans-serif; font-weight: 300;
    font-size: 46px; line-height: 1.0; letter-spacing: -0.5px;
    text-transform: uppercase;
  }
  .card--front .brand { top: 280px; }
  .card--front .brand__mark { background: var(--paper); }
  .card--front .brand__name { color: var(--paper); }
  .card--back .brand { top: 100px; }
  .card--back .brand__mark { background: var(--brand-red); }
  .card--back .brand__name { color: var(--ink); }

  .brand__tagline {
    margin-top: 14px; width: 240px;
    border-top: 2px solid var(--rule-soft); padding-top: 8px;
    font-family: "Roboto Condensed", sans-serif; font-weight: 400;
    font-size: 15.5px; line-height: 1.2; letter-spacing: 1.1px; color: var(--muted);
    text-transform: uppercase; white-space: nowrap;
  }

  /* Front footer */
  .studio-address {
    position: absolute; left: 0; right: 0; top: 680px;
    text-align: center; font-family: "Catamaran", sans-serif; font-style: normal;
  }
  .studio-address__name { font-size: 20px; font-weight: 400; letter-spacing: 0.6px; text-transform: uppercase; }
  .studio-address__rule { width: 236px; height: 2px; margin: 11px auto 14px; background: rgba(255,255,255,0.28); }
  .studio-address__lines { font-size: 20px; line-height: 40px; font-weight: 400; }

  /* Back contacts */
  .contacts { position: absolute; left: 0; right: 0; top: 540px; list-style: none; }
  .contact {
    display: flex; flex-direction: column; align-items: center;
    font-family: "Catamaran", sans-serif; font-size: 20px; font-weight: 500;
    margin-bottom: 12px;
  }
  .contact__divider { display: flex; align-items: center; gap: 14px; margin-bottom: 8px; }
  .contact__divider::before, .contact__divider::after {
    content: ""; width: 52px; height: 2px; background: var(--brand-red);
  }
  .contact__icon { width: 26px; height: 26px; }
  .contact__value { line-height: 28px; }
  .contact__value--phone { letter-spacing: 2px; }
  .contact__accent { color: var(--brand-red); }
</style>
</head>
<body>
<main class="canvas">

  <section class="card card--front" aria-label="Business card front">
    <div class="brand">
      <span class="brand__mark" aria-hidden="true"></span>
      <p class="brand__name">Bramble<br>Orchid<br>Studio</p>
    </div>
    <address class="studio-address">
      <p class="studio-address__name">Bramble Orchid Studio</p>
      <div class="studio-address__rule"></div>
      <p class="studio-address__lines">512 Larkspur Commons Way Suite 210 Marlow<br>Georgia 30999 USA</p>
    </address>
  </section>

  <section class="card card--back" aria-label="Business card back">
    <div class="brand">
      <span class="brand__mark" aria-hidden="true"></span>
      <p class="brand__name">Bramble<br>Orchid<br>Studio</p>
      <p class="brand__tagline">Lighting for Architecture</p>
    </div>

    <ul class="contacts">
      <li class="contact">
        <span class="contact__divider">
          <svg class="contact__icon" viewBox="0 0 26 26" aria-hidden="true">
            <circle cx="13" cy="13" r="13" fill="var(--brand-red)"/>
            <path d="M9 7.5c.6-.5 1.4-.4 1.8.2l1.2 1.9c.3.5.2 1.1-.2 1.5l-.8.7c.6 1.4 1.7 2.6 3.1 3.2l.7-.8c.4-.4 1-.5 1.5-.2l1.9 1.2c.6.4.7 1.2.2 1.8l-.8.9c-.6.6-1.5.8-2.3.5-3.3-1.2-5.8-3.8-7-7-.3-.8-.1-1.7.5-2.3z" fill="#fff"/>
          </svg>
        </span>
        <span class="contact__value contact__value--phone">555.014.2286</span>
      </li>
      <li class="contact">
        <span class="contact__divider">
          <svg class="contact__icon" viewBox="0 0 26 26" aria-hidden="true">
            <circle cx="13" cy="13" r="13" fill="var(--brand-red)"/>
            <rect x="7" y="8.5" width="12" height="9" fill="none" stroke="#fff" stroke-width="1.4"/>
            <path d="M7 8.5l6 5 6-5M7 17.5l4.5-4.3M19 17.5l-4.5-4.3" fill="none" stroke="#fff" stroke-width="1.2"/>
          </svg>
        </span>
        <span class="contact__value">maren@brambleorchidstudio.example</span>
      </li>
      <li class="contact">
        <span class="contact__divider">
          <svg class="contact__icon" viewBox="0 0 26 26" aria-hidden="true">
            <circle cx="13" cy="13" r="13" fill="var(--brand-red)"/>
            <g fill="none" stroke="#fff" stroke-width="1.2">
              <circle cx="13" cy="13" r="6.5"/>
              <ellipse cx="13" cy="13" rx="2.8" ry="6.5"/>
              <path d="M6.5 13h13M7.5 9.8h11M7.5 16.2h11"/>
            </g>
          </svg>
        </span>
        <span class="contact__value">www.<span class="contact__accent">brambleorchidstudio</span>.example</span>
      </li>
    </ul>
  </section>

</main>
</body>
</html>
```